Business Card for premium dental clinic

We are a premium dental clinic based in Brasov, Romania with more than 15 year on the market, providing quality dental treatment made by a team of more specialized dentists, working with modern equipment as a solution to beautiful and healthy teeth.

Our current logo for the clinic use 2 square with colors black and gold - dr Corbescu - studio, using family fonts Bodoni, Myriad Pro and Segoe Print.
Depending on the printing we used some gold CMYK background or gold foil picture background or a gold gradient.
We want a business card:
- eye catching business card
- distinguished business card
- premium design
- to keep the color scheme of black and gold
- to attract the customers to spent time reading the information
- modern concept

```html
<!DOCTYPE html>
<html lang="en">
<head>
<meta charset="utf-8">
<title>Dr. Corbescu Studio – Business Card</title>
<link href="https://fonts.googleapis.com/css2?family=Open+Sans:wght@400;600&family=Roboto+Condensed:wght@700&display=swap" rel="stylesheet">
<style>
  :root {
    --bg: #e4e5e7;
    --black: #0b0b0b;
    --white: #ffffff;
    --gold-dark: #a8761a;
    --gold: #d9a925;
    --gold-light: #f4dc6a;
    --gold-text: #d6a53a;
  }
  * { margin: 0; padding: 0; box-sizing: border-box; }
  html, body { width: 1200px; height: 1021px; overflow: hidden; }
  body {
    background: var(--bg);
    font-family: "Open Sans", sans-serif;
    position: relative;
  }
  .card {
    position: absolute;
    left: 300px;
    width: 600px;
    height: 340px;
    box-shadow: 0 6px 18px rgba(0,0,0,0.18);
  }
  /* Front */
  .card-front {
    top: 140px;
    padding: 22px;
    background: linear-gradient(100deg, var(--gold-dark) 0%, var(--gold) 25%, var(--gold-light) 45%, var(--gold) 60%, var(--gold-dark) 80%, var(--gold) 100%);
  }
  .front-inner {
    position: relative;
    width: 100%;
    height: 100%;
    border: 3px solid var(--white);
    display: flex;
  }
  .gold-foil {
    width: 50%;
    height: 100%;
    background: radial-gradient(ellipse at 40% 40%, var(--gold-light) 0%, var(--gold) 55%, #c58f18 100%);
  }
  .black-square {
    width: 50%;
    height: 100%;
    background: var(--black);
    position: relative;
  }
  .name-box {
    position: absolute;
    left: 32px;
    top: 62px;
    width: 240px;
    height: 70px;
    background: var(--white);
    display: flex;
    align-items: center;
    justify-content: center;
  }
  .clinic-name {
    font-family: "Open Sans", sans-serif;
    font-weight: 400;
    font-size: 34px;
    color: var(--black);
    letter-spacing: -0.5px;
  }
  .studio {
    position: absolute;
    left: 40px;
    top: 92px;
    font-family: "Open Sans", sans-serif;
    font-weight: 400;
    font-size: 42px;
    color: var(--white);
  }
  .tagline {
    position: absolute;
    right: 14px;
    bottom: 10px;
    font-family: "Roboto Condensed", sans-serif;
    font-weight: 700;
    font-size: 30px;
    color: var(--white);
  }
  /* Back */
  .card-back {
    top: 540px;
    background: var(--black);
  }
  .back-title {
    position: absolute;
    left: 80px;
    top: 110px;
    font-size: 24px;
    font-weight: 400;
    color: var(--gold-text);
  }
  .address {
    position: absolute;
    left: 80px;
    top: 150px;
    font-size: 15px;
    line-height: 21px;
    color: var(--white);
  }
  .divider {
    position: absolute;
    left: 326px;
    top: 110px;
    width: 2px;
    height: 100px;
    background: var(--gold-text);
  }
  .contact-list {
    position: absolute;
    left: 344px;
    top: 116px;
    list-style: none;
  }
  .contact-item {
    display: flex;
    align-items: center;
    gap: 10px;
    font-size: 15px;
    line-height: 23px;
    color: var(--white);
  }
  .contact-icon { width: 14px; height: 14px; flex: none; }
</style>
</head>
<body>
  <section class="card card-front">
    <div class="front-inner">
      <div class="gold-foil" role="img" aria-label="Crumpled gold foil texture"></div>
      <div class="black-square">
        <span class="studio">studio</span>
        <span class="tagline">dental clinic</span>
      </div>
      <div class="name-box"><span class="clinic-name">dr Corbescu</span></div>
    </div>
  </section>

  <section class="card card-back">
    <h1 class="back-title">Dr. Corbescu Studio</h1>
    <p class="address">strada Livezii nr 8<br>Brasov, Romania 500210</p>
    <div class="divider"></div>
    <ul class="contact-list">
      <li class="contact-item">
        <svg class="contact-icon" viewBox="0 0 14 14"><rect x="3.5" y="0.8" width="7" height="12.4" rx="1.2" fill="none" stroke="#d6a53a" stroke-width="1.3"/><line x1="6" y1="11" x2="8" y2="11" stroke="#d6a53a" stroke-width="1.2"/></svg>
        +40 700 555 018
      </li>
      <li class="contact-item">
        <svg class="contact-icon" viewBox="0 0 14 14"><path d="M3 1 L5.5 4 L4 5.5 Q5.5 8.5 8.5 10 L10 8.5 L13 11 L11 13 Q5 12 1 3 Z" fill="#d6a53a"/></svg>
        +40 268 555 042
      </li>
      <li class="contact-item">
        <svg class="contact-icon" viewBox="0 0 14 14"><rect x="1" y="3" width="12" height="8.5" fill="none" stroke="#d6a53a" stroke-width="1.3"/><polyline points="1,3 7,8 13,3" fill="none" stroke="#d6a53a" stroke-width="1.3"/></svg>
        info@drcorbescu.ro
      </li>
      <li class="contact-item">
        <svg class="contact-icon" viewBox="0 0 14 14"><circle cx="7" cy="7" r="6" fill="none" stroke="#d6a53a" stroke-width="1.2"/><ellipse cx="7" cy="7" rx="2.6" ry="6" fill="none" stroke="#d6a53a" stroke-width="1"/><line x1="1" y1="7" x2="13" y2="7" stroke="#d6a53a" stroke-width="1"/></svg>
        www.drcorbescu.ro
      </li>
    </ul>
  </section>
</body>
</html>
```